Tallyleaf Web Design

Create Website Design for Tallyleaf. Tallyleaf is online application for collaboration team work system (task list management). More concept design for this project please find attach file ("tallyleaf website concept.pdf") . But my concept is just describe minimal features not bind design

For tallyleaf logo, i had already attach files. But i had not decided what color i chose, so it's okay if you suggest logo color for your suitable website design.
Updates

Dear All Designer,

I like brisk carousel (http://quorvanlabs.example/brisk-carousel/),
may be your concept design can adjust with this concept.
but don't worry about script for brisk carousel, my team will be handle
You just make website design to suitable with brisk carousel

but if you had own website design concept are welcome

thanks

Target Market(s)

Business Company

Industry/Entity Type

Management

```html
<!DOCTYPE html>
<html lang="en">
<head>
<meta charset="utf-8">
<title>Tallyleaf — Collaboration Solution</title>
<link href="https://fonts.googleapis.com/css2?family=Oswald:wght@400;500;600&family=Roboto+Condensed:wght@400&family=Arimo:wght@400;700&display=swap" rel="stylesheet">
<style>
:root{
  --cream:#f4eee3;
  --cream-dark:#e9e1d4;
  --footer:#e4ddd3;
  --blue:#246791;
  --purple:#8c1a7d;
  --purple-light:#a8279a;
  --orange:#d48a1c;
  --teal:#2c7c72;
  --nav:#4d4b48;
  --ink:#222;
  --muted:#555;
  --gold:#f0b43a;
}
*{box-sizing:border-box;margin:0;padding:0}
html,body{width:945px;height:1200px;overflow:hidden}
body{background:var(--cream);font-family:"Roboto Condensed",sans-serif;color:var(--ink)}
.canvas{position:relative;width:945px;height:1200px;overflow:hidden;
  background:repeating-linear-gradient(0deg,rgba(0,0,0,.018) 0 1px,transparent 1px 9px),
             repeating-linear-gradient(90deg,rgba(0,0,0,.018) 0 1px,transparent 1px 9px),var(--cream)}
.abs{position:absolute}
.account-tab{left:755px;top:0;width:163px;height:28px;background:#e8d3ac;border-radius:0 0 8px 8px;display:flex;font-family:Arimo,sans-serif;font-size:13px}
.account-tab span{flex:1;text-align:center;line-height:26px}
.account-tab .login{background:#f1ddb5;color:#222;border-radius:0 0 0 8px}
.account-tab .signup{color:#fff}
.brand{left:18px;top:22px;display:flex;align-items:center;gap:10px;font-family:Arimo,sans-serif;font-weight:700;font-size:46px;color:var(--teal);letter-spacing:-1px}
.brand i{width:34px;height:34px;border-radius:50%;background:var(--purple);display:block}
.nav{left:448px;top:45px;display:flex;gap:10px}
.nav a{font-family:Oswald,sans-serif;font-size:17px;color:#fff;text-decoration:none;background:var(--nav);border:1px solid #2e2d2b;border-radius:3px;height:30px;line-height:28px;padding:0 9px;box-shadow:inset 0 1px 0 rgba(255,255,255,.25)}
.nav a.active{background:var(--orange);border-color:#9d6210;position:relative}
.nav a.active::after{content:"";position:absolute;left:50%;bottom:-7px;margin-left:-6px;border:6px solid transparent;border-top-color:#9d6210;border-bottom:0}
.video{left:19px;top:135px;width:455px;height:269px;border:3px solid #4d7d9a;background:linear-gradient(135deg,#2d3945,#1d2329 55%,#2b3440)}
.video svg{position:absolute;left:207px;top:114px}
.hero-title{left:505px;top:144px;width:400px;text-align:center;font-family:Oswald,sans-serif;font-weight:600;line-height:44px;font-size:42px}
.hero-title .accent{color:var(--purple)}
.hero-sub{left:490px;top:242px;width:440px;text-align:center;font-family:Oswald,sans-serif;font-weight:400;font-size:23px;color:#333}
.cta{left:564px;top:294px;width:283px;height:103px;border-radius:8px;background:linear-gradient(var(--purple-light),var(--purple));border:2px solid #fff;box-shadow:0 2px 5px rgba(0,0,0,.35);text-align:center;font-family:Oswald,sans-serif;font-size:23px;line-height:36px;padding-top:13px;color:#fff}
.cta .top{color:var(--gold)}
.welcome-bar{left:19px;top:441px;width:909px;height:32px;background:var(--blue);color:#fff;font-family:Oswald,sans-serif;font-weight:500;font-size:18px;line-height:32px;padding-left:18px}
.welcome-text{left:19px;top:483px;width:909px;height:180px;padding:6px 18px 0;background:rgba(255,255,255,.35);font-size:11px;line-height:18.2px;color:#333;text-align:justify}
.welcome-text p{border-bottom:1px solid #e3ddd3}
.read-more{left:851px;top:641px;font-size:12px;color:var(--blue)}
.feature{top:682px;width:281px;height:216px;background:#fff;border:1px solid #ddd;box-shadow:0 10px 10px -8px rgba(0,0,0,.25)}
.feature .head{height:44px;display:flex;align-items:center;color:#fff;font-family:Oswald,sans-serif;font-weight:500;font-size:18px}
.feature .toggle{width:40px;height:44px;background:#111;color:#fff;display:flex;align-items:center;justify-content:center;font-size:26px;margin-right:16px}
.feature .pic{margin:3px;height:163px}
.f-custom{left:19px;background:var(--orange);border-color:var(--orange)}
.f-custom .head{background:var(--orange)}
.f-custom .body{padding:10px 17px 0 18px;font-size:11.5px;line-height:18.2px;text-align:justify;color:#2a1a05}
.f-custom .link{position:absolute;right:0;bottom:0;width:34px;height:36px;background:#111}
.f-sync{left:334px}.f-sync .head{background:var(--purple)}
.f-report{left:646px}.f-report .head{background:var(--teal)}
.f-report .title{flex:1;text-align:center;padding-right:56px}
.footer{left:0;top:918px;width:945px;height:282px;background:var(--footer)}
.footer-edge{left:0;top:900px}
.col{top:968px;font-family:Arimo,sans-serif}
.col h4{font-size:14px;font-weight:700;color:#222;margin-bottom:10px}
.col li{list-style:none;font-size:11.5px;color:#555;height:23.6px;display:flex;align-items:center;gap:9px}
.col li::before{content:"";width:7px;height:7px;border:1.5px solid #888;border-radius:50%}
.col li.current{color:var(--teal)}
.col li.current::before{border-color:var(--teal)}
.social li{height:29px}
.social li::before{display:none}
.social li i{width:22px;height:22px;border-radius:50%;background:#3a3f4a;display:block}
.social li i.fb{background:#3c5a96}
.foot-brand{left:0;top:1126px;width:945px;text-align:center;font-family:Arimo,sans-serif;font-weight:700;font-size:34px;color:#8a8580}
.copy{left:0;top:1173px;width:945px;text-align:center;font-family:Arimo,sans-serif;font-size:11.5px;color:#7a4a2a}
</style>
</head>
<body>
<div class="canvas">
  <div class="abs account-tab"><span class="login">Login</span><span class="signup">Singup</span></div>
  <div class="abs brand">tallyleaf<i></i></div>
  <nav class="abs nav">
    <a class="active" href="#">Home</a><a href="#">About Us</a><a href="#">Tour</a><a href="#">Pricing</a><a href="#">Costomers</a><a href="#">Contact Us</a>
  </nav>

  <div class="abs video" role="img" aria-label="Intro video still: globe, notebook and pen on a desk">
    <svg width="42" height="42" viewBox="0 0 42 42"><circle cx="21" cy="21" r="19" fill="none" stroke="#fff" stroke-width="3"/><path d="M16 12 L31 21 L16 30 Z" fill="#fff"/></svg>
  </div>

  <h1 class="abs hero-title">The most complete<br><span class="accent">collaboration solution</span></h1>
  <div class="abs hero-sub">Free up to 5 users · Pro from $5/mo per user</div>
  <div class="abs cta"><div class="top">Get Started With</div><div>a free version of Tallyleaf</div></div>

  <div class="abs welcome-bar">Welcome Tallyleaf!</div>
  <div class="abs welcome-text">
    <p>Lorem ipsum dolor sit amet, consectetur adipiscing elit. Vestibulum accumsan, diam pulvinar fermentum vestibulum, enim felis mollis quam, quis aliquet nisl justo sed neque. Suspendisse potenti. Praesent sed nunc lorem. Class aptent taciti sociosqu ad litora torquent per conubia nostra, per inceptos himenaeos. In vestibulum luctus est non commodo. Donec consectetur urna non magna cursus eget lobortis est egestas. Cras pellentesque leo non est tincidunt quis tempus neque vulputate. Curabitur vitae eros arcu, at luctus metus. Class aptent taciti sociosqu ad litora torquent per conubia nostra, per inceptos himenaeos. Vestibulum tellus nisl, convallis nec elementum nec, tempor eu elit. Morbi mauris libero, iaculis dapibus faucibus ac, scelerisque vel nulla. Phasellus pellentesque blandit sapien eget consectetur</p>
    <p>Lorem ipsum dolor sit amet, consectetur adipiscing elit. Vestibulum accumsan, diam pulvinar fermentum vestibulum, enim felis mollis quam, quis aliquet nisl justo sed neque. Suspendisse potenti. Praesent sed nunc lorem. Class aptent taciti sociosqu ad litora torquent per conubia nostra, per inceptos himenaeos. In vestibulum luctus est non commodo. Donec consectetur urna non magna cursus eget lobortis est egestas. Cras pellentesque leo non est tincidunt quis tempus neque vulputate. Curabitur vitae eros arcu, at luctus metus.</p>
  </div>
  <div class="abs read-more">Read more...</div>

  <section class="abs feature f-custom">
    <div class="head"><span class="toggle">-</span>Customize Application</div>
    <div class="body">Lorem ipsum dolor sit amet, consectetur adipiscing elit. Vestibulum accumsan, diam pulvinar fermentum vestibulum, enim felis mollis quam, quis aliquet nisl justo sed neque. Suspendisse potenti. Praesent sed nunc lorem. Class aptent taciti sociosqu ad litora torquent per conubia nostra, per inceptos himenaeos. In vestibulum luctus est non commodo.</div>
    <div class="link"><svg width="34" height="36" viewBox="0 0 34 36"><g fill="none" stroke="#fff" stroke-width="2.5" stroke-linecap="round"><path d="M15 21 l-4 4 a3.5 3.5 0 0 1 -5 -5 l4 -4"/><path d="M19 15 l4 -4 a3.5 3.5 0 0 1 5 5 l-4 4"/><path d="M14 22 L20 14"/></g></svg></div>
  </section>
  <section class="abs feature f-sync">
    <div class="head"><span class="toggle">+</span>Synchronize All Device</div>
    <div class="pic" role="img" aria-label="Illustration of devices connected to a central blue hub" style="background:radial-gradient(circle at 50% 35%,#7fd0ef 0 8%,#eef0f2 9%,#c9ccd0 70%,#b5b8bc)"></div>
  </section>
  <section class="abs feature f-report">
    <div class="head"><span class="toggle">+</span><span class="title">Report</span></div>
    <div class="pic" role="img" aria-label="Photo of hands with pens reviewing printed reports" style="background:linear-gradient(135deg,#20242c,#6a6f78 45%,#2a2e36 75%,#14161a)"></div>
  </section>

  <svg class="abs footer-edge" width="945" height="24" viewBox="0 0 945 24" preserveAspectRatio="none"><path d="M0 24 L0 10 L40 14 L80 6 L130 15 L190 8 L250 16 L310 7 L370 13 L430 5 L490 14 L550 8 L610 16 L670 6 L730 13 L790 9 L850 15 L900 7 L945 12 L945 24 Z" fill="var(--footer)"/></svg>
  <footer class="abs footer"></footer>

  <div class="abs col" style="left:18px"><h4>Site Links</h4><ul><li class="current">Home</li><li>About Us</li><li>Tour</li><li>Pricing</li><li>Costomers</li><li>Contact Us</li></ul></div>
  <div class="abs col" style="left:208px"><h4>Resources</h4><ul><li>Blog</li><li>Support Center</li><li>F.A.Q</li><li>Developers</li><li>API Documentation</li></ul></div>
  <div class="abs col" style="left:418px"><h4>Products</h4><ul><li>Tallyleaf Tracker</li><li>Free trial</li><li>Why Tallyleaf</li></ul></div>
  <div class="abs col" style="left:637px"><h4>Company</h4><ul><li>Company</li><li>Leadership team</li><li>Careers</li><li>Newsletters</li><li>Contact</li></ul></div>
  <div class="abs col social" style="left:843px"><h4>Socials</h4><ul><li><i class="fb"></i>Friendsphere</li><li><i></i>Chirpline</li><li><i></i>Linkward</li><li><i></i>Mail</li></ul></div>

  <div class="abs foot-brand">tallyleaf</div>
  <div class="abs copy">Copyright © 2013, Tallyleaf</div>
</div>
</body>
</html>
```